FernPivotHub.com needs updated website design.

FernPivotHub.com offers individuals a quick, hassle-free way of selling their car, rv, or boat in the Sun City Center, FL area. We will come to the customer's place of choosing in order to give them an in-person offer for their car, rv, or boat. Looking for a website design that will allow users to input their vehicle details as well as their contact info in order to schedule a time and place for our staff to come make them an offer. Currently have an active site that can be referenced.

Target Market(s)

Older people who no longer need their cars.

Industry/Entity Type

Automotive

Coding

Coded - Design and coding required

Number of Pages Required

3 page

Font styles to use
Sans Serif

Colors
a1cd3a
33b8a4

Requirements
Must have
• Trustworthy theme, Emphasis on capturing contact info (contact form visible at all times). Standard privacy policy. Wordpress theme

```html
<!DOCTYPE html>
<html lang="en">
<head>
<meta charset="utf-8">
<title>FernPivotHub.com — Get Your Free In Person Cash Offer Today</title>
<link href="https://fonts.googleapis.com/css2?family=Montserrat:wght@400;500;600;700&family=Righteous&family=Open+Sans:wght@400;600;700&display=swap" rel="stylesheet">
<style>
:root{
  --teal:#33b8a4;
  --green:#a1cd3a;
  --dark:#2b2b2b;
  --panel:#333333;
  --text:#555555;
  --white:#ffffff;
}
*{box-sizing:border-box;margin:0;padding:0}
html,body{width:1200px;height:3571px;overflow:hidden}
body{position:relative;background:var(--white);font-family:'Montserrat',sans-serif;color:var(--text)}
.abs{position:absolute}
.btn{position:absolute;display:flex;align-items:center;justify-content:center;background:var(--green);color:var(--white);font:600 12px 'Montserrat',sans-serif;text-transform:uppercase}

/* hero */
.hero{left:0;top:8px;width:1200px;height:789px;background:linear-gradient(100deg,#4a4642 0%,#6b6560 40%,#77736d 70%,#5e5a55 100%)}
.topline{left:0;top:0;width:1200px;height:8px;background:#ffffff}
.brand{position:absolute;display:flex;align-items:center;gap:10px}
.brand-text{text-align:right;color:var(--white);font-family:'Open Sans',sans-serif;font-weight:700;line-height:1.2}
.brand-mark{border-radius:50%;background:var(--teal)}
.nav{left:424px;top:62px;display:flex;gap:18px;font:15px 'Righteous',sans-serif;color:var(--white)}
.nav span:first-child{margin-right:20px}
.sell-now{left:967px;top:46px;width:208px;height:54px;background:linear-gradient(90deg,var(--teal),var(--green));font-size:16px}
.welcome-tag{left:0;top:264px;width:1200px;text-align:center;font:18px 'Righteous',sans-serif;color:var(--teal)}
.headline{left:0;top:312px;width:1200px;text-align:center;font:400 70px/86px 'Righteous',sans-serif;color:var(--white);letter-spacing:2px}

/* cards */
.card{position:absolute;top:628px;width:300px;height:344px;background:var(--panel);border-radius:4px;box-shadow:0 4px 10px rgba(0,0,0,.25);text-align:center}
.card-photo{position:absolute;left:9px;top:8px;width:282px;height:158px}
.card h3{position:absolute;top:182px;width:100%;font:600 15px 'Montserrat',sans-serif;color:var(--teal);text-transform:uppercase}
.card p{position:absolute;top:216px;left:52px;width:196px;font:12px/22px 'Open Sans',sans-serif;color:var(--white)}
.card .btn{left:62px;top:300px;width:176px;height:34px}

/* welcome */
.wel-title{left:180px;top:1086px;width:546px;text-align:center;font:700 41px/40px 'Montserrat',sans-serif;color:var(--teal)}
.rule{position:absolute;height:1px;background:#9a9a9a}
.rule.light{background:rgba(255,255,255,.8)}
.wel-lead{left:213px;top:1250px;width:480px;text-align:center;font:13px/22px 'Montserrat',sans-serif;color:#888}
.wel-body{left:170px;top:1311px;width:566px;text-align:center;font:12.5px/22px 'Montserrat',sans-serif;color:#444}
.side-form{left:798px;top:1081px;width:271px;height:358px;background:var(--panel);border-radius:12px}
.field{position:absolute;border:1px solid var(--teal);font:14px 'Montserrat',sans-serif;color:#8a9a9a;padding:7px 10px}
.side-form .field{left:20px;width:232px;height:37px;border-radius:2px}

/* bands */
.band{position:absolute;left:0;width:1200px;text-align:center}
.band-bg{position:absolute;inset:0}
.band h2{position:absolute;width:100%;font:700 41px 'Montserrat',sans-serif;color:var(--teal);text-transform:uppercase}
.band p{position:absolute;width:100%;font:500 21px/35px 'Montserrat',sans-serif;color:var(--white)}
.wedge{position:absolute;left:0;width:1200px}

/* contact block */
.promo{left:100px;top:2697px;width:535px;height:336px;background:linear-gradient(135deg,#3a3a3a,#5a5a5a 50%,#2f2f2f)}
.promo-name{left:150px;top:2830px;font:700 36px 'Open Sans',sans-serif;color:var(--white)}
.promo-sub{left:119px;top:2874px;font:700 24px 'Open Sans',sans-serif;color:var(--white)}
.promo-dot{left:488px;top:2808px;width:126px;height:126px;border-radius:50%;background:var(--teal)}
.lead-form .field{left:672px;width:333px;height:37px;border-radius:2px;color:#9aa}

/* quote */
.quote{left:108px;top:3122px;font:28px 'Righteous',sans-serif;color:var(--teal)}
.quote-note{left:108px;top:3174px;width:455px;font:11.5px/19px 'Montserrat',sans-serif;color:#333;text-transform:uppercase}

/* footer */
.footer{left:0;top:3243px;width:1200px;height:328px;background:var(--dark)}
.fcol{position:absolute;text-align:center;color:var(--white);font:500 13px 'Montserrat',sans-serif}
.fcol h4{font:700 23px 'Montserrat',sans-serif;color:var(--teal);margin-bottom:20px}
.fcol li{list-style:none;height:31px}
.social{display:flex;gap:27px;justify-content:center;margin-top:18px}
.social i{display:block;width:10px;height:10px;border-radius:50%;background:var(--green)}
.up{left:1152px;top:3523px;width:36px;height:36px;background:#222;color:var(--white);font:14px sans-serif;display:flex;align-items:center;justify-content:center}
</style>
</head>
<body>

<div class="abs topline"></div>
<div class="abs hero" role="img" aria-label="Photo of a hand handing over car keys while another hand offers a stack of cash"></div>

<div class="brand" style="left:58px;top:46px">
  <div class="brand-text"><div style="font-size:20px">FernPivotHub.com</div><div style="font-size:12.5px">I'll Buy You Car Boat RV Today</div></div>
  <div class="brand-mark" style="width:56px;height:56px"></div>
</div>
<nav class="abs nav"><span>Home</span><span>About</span><span>Pricing</span><span>Services</span><span>Stories</span><span>Blogs</span><span>Contact</span></nav>
<div class="btn sell-now">Sell Now &nbsp;
  <svg width="18" height="12" viewBox="0 0 18 12"><path d="M1 6h15M11 1l5 5-5 5" stroke="#fff" stroke-width="1.8" fill="none"/></svg></div>

<div class="abs welcome-tag">Welcome To FernPivotHub.Com</div>
<h1 class="abs headline">Get Your Free In Person<br>Cash Offer Today</h1>

<div class="card" style="left:118px">
  <div class="card-photo" role="img" aria-label="Red sports car lit in neon colours" style="background:linear-gradient(120deg,#c21030,#3a1020 50%,#0f6d74)"></div>
  <h3>Car Selling</h3>
  <p><b>Lorem Ipsum</b> is simply dummy text of the printing and typesetting industry.</p>
  <div class="btn">Get Offer Now</div>
</div>
<div class="card" style="left:453px">
  <div class="card-photo" role="img" aria-label="White motorhome RV" style="background:linear-gradient(180deg,#ffffff,#ececec 60%,#cfcfcf)"></div>
  <h3>RV Selling</h3>
  <p><b>Lorem Ipsum</b> is simply dummy text of the printing and typesetting industry.</p>
  <div class="btn">Get Offer Now</div>
</div>
<div class="card" style="left:789px">
  <div class="card-photo" role="img" aria-label="Speedboat cutting through blue water" style="background:linear-gradient(160deg,#e9c9a0,#4fa6c8 45%,#1d5f9e)"></div>
  <h3>Boats Selling</h3>
  <p><b>Lorem Ipsum</b> is simply dummy text of the printing and typesetting industry.</p>
  <div class="btn">Get Offer Now</div>
</div>

<h2 class="abs wel-title">WELCOME TO<br>FERNPIVOTHUB.COM</h2>
<div class="rule" style="left:272px;top:1206px;width:364px"></div>
<p class="abs wel-lead">Lorem Ipsum Is Mostly A Part Of A Latin Text By The Classical Author And Philosopher Cicero.</p>
<p class="abs wel-body">We Offer The Most Convenient Way Of Selling Your Vehicle. We Will Come To You At A Place Of Your Choosing, I.E. Home, Office, Or Any Other Public Place. We Will Give You An In Person Cash Offer On The Spot.</p>
<div class="btn" style="left:377px;top:1394px;width:152px;height:35px">Learn More</div>

<div class="abs side-form">
  <div class="field" style="top:20px">Name</div>
  <div class="field" style="top:76px">Email</div>
  <div class="field" style="top:131px">Contact</div>
  <div class="field" style="top:187px;height:99px">Message</div>
  <div class="btn" style="left:20px;top:304px;width:112px;height:34px">Submi</div>
</div>

<section class="band" style="top:1491px;height:380px">
  <div class="band-bg" role="img" aria-label="Old beaten pale green car parked on a city street" style="background:linear-gradient(90deg,#3f3f38,#5c5b4c 40%,#6a6856 60%,#45463f)"></div>
  <h2 style="top:80px">Old Clunckers</h2>
  <div class="rule light" style="left:466px;top:160px;width:268px"></div>
  <p style="top:208px">Got An Old Clunker? I'll But It! – Turn It Into Cash Today!</p>
  <div class="btn" style="left:513px;top:258px;width:180px;height:36px">Sell Clunckers</div>
</section>
<section class="band" style="top:1871px;height:381px">
  <div class="band-bg" role="img" aria-label="Hand holding car keys above a pile of cash" style="background:linear-gradient(90deg,#364a55,#5a6a70 40%,#75705f 70%,#3c4a52)"></div>
  <h2 style="top:62px">Stop Wasting Money On Insurance</h2>
  <div class="rule light" style="left:292px;top:144px;width:620px"></div>
  <p style="top:188px">Got A Nice Car You Just Don't Need? I'll Buy It! – Stop Wasting Money On<br>Insurance, Registration And Maintenance Costs!</p>
  <div class="btn" style="left:517px;top:279px;width:171px;height:36px">Sell Nice Cars</div>
</section>
<section class="band" style="top:2252px;height:381px">
  <div class="band-bg" role="img" aria-label="Stressed driver sitting in front of a broken-down white car with the hood open" style="background:linear-gradient(90deg,#b7bcc0,#3d3f44 30%,#2c2d31 60%,#5a5e63)"></div>
  <h2 style="top:74px">I'll Buy It</h2>
  <div class="rule light" style="left:520px;top:154px;width:166px"></div>
  <p style="top:194px">Got A Car That Needs Repairs? I'll Buy It! – No Matter What The Issue Is I'll<br>Come Take It Away Today!</p>
  <div class="btn" style="left:535px;top:278px;width:136px;height:36px">Sell Now</div>
</section>
<svg class="wedge" style="top:1838px" width="1200" height="34" viewBox="0 0 1200 34"><path d="M0 34 Q300 26 600 0 Q900 26 1200 34 Z" fill="#a1cd3a"/></svg>
<svg class="wedge" style="top:2222px" width="1200" height="32" viewBox="0 0 1200 32"><path d="M0 32 Q300 24 600 0 Q900 24 1200 32 Z" fill="#a1cd3a"/></svg>

<div class="abs promo" role="img" aria-label="Laptop and phone on a desk, dimmed behind the brand name"></div>
<div class="abs promo-name">FernPivotHub.com</div>
<div class="abs promo-sub">I'll Buy You Car Boat RV Today</div>
<div class="abs promo-dot"></div>

<div class="lead-form">
  <div class="field" style="top:2736px">Enter Your Vehical Detail</div>
  <div class="field" style="top:2792px">Enter Your Email</div>
  <div class="field" style="top:2847px">Enter Your Contact Number</div>
  <div class="field" style="top:2903px">Enter Description</div>
  <div class="btn" style="left:672px;top:2958px;width:152px;height:35px">Learn More</div>
</div>

<div class="abs quote">“Don't Sell Til You Give Me A Yell”</div>
<p class="abs quote-note">Lorem Ipsum Is Mostly A Part Of A Latin Text By The Classical Author And Philosopher Cicero.</p>
<div class="btn" style="left:876px;top:3150px;width:166px;height:39px">Get Paid Now</div>

<footer class="abs footer">
  <div class="brand" style="left:114px;top:68px">
    <div class="brand-text"><div style="font-size:23px">FernPivotHub.com</div><div style="font-size:14px">I'll Buy You Car Boat RV Today</div></div>
    <div class="brand-mark" style="width:64px;height:64px"></div>
  </div>
  <div class="fcol" style="left:120px;top:160px;width:292px;font-size:12.5px">Get Your Free In Person Cash Offer Today
    <div style="margin-top:17px;font-weight:700;font-size:15px;letter-spacing:1px">follow us</div>
    <div class="social"><i></i><i></i><i></i><i></i></div>
  </div>
  <div class="fcol" style="left:464px;top:64px;width:140px"><h4>MENUS</h4>
    <ul><li>Home</li><li>About</li><li>Pricing</li><li>Services</li><li>Contact Us</li></ul></div>
  <div class="fcol" style="left:630px;top:64px;width:226px"><h4>OUR BLOG</h4>
    <ul style="line-height:14px"><li style="height:42px">Most People Who Order</li><li style="height:42px">To Get More Efficieny</li><li>How To Improve Selling</li></ul></div>
  <div class="fcol" style="left:900px;top:64px;width:176px"><h4>GET INFO</h4>
    <div style="display:flex;gap:10px;justify-content:center;align-items:center">
      <svg width="12" height="12" viewBox="0 0 24 24"><path d="M6.6 10.8a15 15 0 006.6 6.6l2.2-2.2c.3-.3.7-.4 1-.2 1.1.4 2.3.6 3.6.6.6 0 1 .4 1 1V20c0 .6-.4 1-1 1A17 17 0 013 4c0-.6.4-1 1-1h3.5c.6 0 1 .4 1 1 0 1.3.2 2.5.6 3.6.1.3 0 .7-.2 1z" fill="#33b8a4"/></svg>555-014-2290</div>
    <div style="display:flex;gap:10px;justify-content:center;align-items:center;margin-top:40px">
      <svg width="13" height="10" viewBox="0 0 13 10"><rect x=".5" y=".5" width="12" height="9" fill="none" stroke="#33b8a4"/><path d="M.5 .5l6 5 6-5" fill="none" stroke="#33b8a4"/></svg>hello@fernpivothub.com</div>
  </div>
</footer>
<div class="abs up">&#9650;</div>

</body>
</html>
```